Qorvane Management LLC Business Card

The sample logo was attached for the business Card Design for Traffic Control Company named Qorvane Management LLC. Card design needs to have the company logo and colors match the logo color. It will be nice to show some images of Traffic control signs or cones, even roads closer that math the company services

Target Market(s)

Temporary traffic control. Road closer.

Industry/Entity Type

Construction

Contact Information for Business Card

basic information, name, job title, address, email phone, website

Font styles to use
Serif
Sans Serif

Colors
F0912C
F2A743
F7CA91
FBE8D2
FDF5EE
EE7325
F08F49
F5BC92
FAE3D3
FDF4ED

```html
<!DOCTYPE html>
<html lang="en">
<head>
<meta charset="utf-8">
<title>Qorvane Management LLC – Business Card</title>
<link href="https://fonts.googleapis.com/css2?family=Montserrat:wght@400;500;700&display=swap" rel="stylesheet">
<style>
  :root {
    --backdrop: #e9e9ea;
    --card: #ffffff;
    --orange: #ee7325;
    --orange-soft: #f08f49;
    --cone-light: #f5bc92;
    --cone-pale: #fae3d3;
    --ink: #1f1f1f;
    --ink-soft: #444444;
  }
  * { box-sizing: border-box; margin: 0; padding: 0; }
  html, body {
    width: 1200px; height: 900px; overflow: hidden;
    background: var(--backdrop);
    font-family: "Montserrat", sans-serif;
    color: var(--ink);
  }
  .canvas {
    width: 1200px; height: 900px;
    display: flex; flex-direction: column;
    align-items: center; justify-content: center; gap: 40px;
  }
  .card {
    width: 680px; height: 388px;
    background: var(--card);
    box-shadow: 0 6px 18px rgba(0,0,0,.12);
    position: relative;
  }
  .brand {
    display: flex; align-items: center; gap: 12px;
    font-weight: 700; color: var(--orange);
    letter-spacing: .02em; white-space: nowrap;
  }
  .brand__mark { width: 14px; height: 14px; background: var(--orange); flex: none; }
  /* Front */
  .card--front {
    display: flex; flex-direction: column; align-items: center; justify-content: center; gap: 28px;
  }
  .signs-illustration {
    width: 300px; height: 110px;
    background: linear-gradient(90deg, var(--cone-pale), var(--cone-light) 40%, var(--orange-soft) 70%, var(--cone-pale));
    border-radius: 6px;
  }
  .card--front .brand { font-size: 30px; }
  /* Back */
  .card--back { padding: 60px 40px 40px; }
  .back__body { display: flex; align-items: center; height: 230px; }
  .back__brand { width: 290px; display: flex; justify-content: center; }
  .card--back .brand { font-size: 17px; gap: 10px; }
  .card--back .brand__mark { width: 12px; height: 12px; }
  .divider { width: 2px; height: 170px; background: var(--orange-soft); margin: 0 24px; flex: none; }
  .contact { font-size: 14px; line-height: 1.45; color: var(--ink-soft); }
  .contact__name { color: var(--orange); font-weight: 700; font-size: 18px; text-transform: uppercase; letter-spacing: .03em; }
  .contact__role, .contact__address { color: var(--ink); }
  .contact__list { list-style: none; margin-top: 8px; }
  .contact__list li { display: flex; align-items: center; gap: 10px; color: var(--ink); white-space: nowrap; }
  .contact__list svg { width: 13px; height: 13px; flex: none; }
  .tagline {
    position: absolute; left: 0; right: 0; bottom: 44px;
    text-align: center; font-size: 14px; font-weight: 500; color: var(--ink);
  }
</style>
</head>
<body>
<main class="canvas">
  <section class="card card--front">
    <div class="signs-illustration" role="img" aria-label="Illustration of traffic cones, a road closure sign and a detour arrow sign"></div>
    <div class="brand"><span class="brand__mark"></span><span>Qorvane Management LLC</span></div>
  </section>

  <section class="card card--back">
    <div class="back__body">
      <div class="back__brand">
        <div class="brand"><span class="brand__mark"></span><span>Qorvane Management LLC</span></div>
      </div>
      <div class="divider"></div>
      <div class="contact">
        <p class="contact__name">Dorian Halvik</p>
        <p class="contact__role">Owner/Director</p>
        <p class="contact__address">Halden Court 1780 Riverside<br>Tolva Rd Suite 310</p>
        <ul class="contact__list">
          <li>
            <svg viewBox="0 0 16 16" aria-hidden="true"><circle cx="8" cy="8" r="8" fill="#ee7325"/><path d="M5 4.5c.5-.5 1.2-.3 1.4.2l.6 1.3c.1.4 0 .7-.3.9l-.5.4c.5 1 1.3 1.8 2.3 2.3l.4-.5c.2-.3.6-.4.9-.3l1.3.6c.5.2.7.9.2 1.4-.9.9-2.2 1-3.4.2C6.6 10.2 5.8 9.4 5 8.1 4.2 6.8 4.2 5.4 5 4.5z" fill="#fff"/></svg>
            555-014-2290
          </li>
          <li>
            <svg viewBox="0 0 16 16" aria-hidden="true"><rect x="1" y="3" width="14" height="10" rx="1" fill="#ee7325"/><path d="M1.5 4 8 9l6.5-5" stroke="#fff" stroke-width="1.2" fill="none"/></svg>
            info@qorvanemanagement.com
          </li>
          <li>
            <svg viewBox="0 0 16 16" aria-hidden="true"><circle cx="8" cy="8" r="7" fill="#ee7325"/><path d="M1 8h14M8 1c-2.5 2.5-2.5 11.5 0 14M8 1c2.5 2.5 2.5 11.5 0 14" stroke="#fff" stroke-width="1" fill="none"/></svg>
            www.qorvanemanagement.com
          </li>
        </ul>
      </div>
    </div>
    <p class="tagline">Traffic Control Company named Qorvane Management LLC.</p>
  </section>
</main>
</body>
</html>
```